New Corporate Business Card - Velmorabelle

What we need:
We need a new corporate business card.
We want a new template that we can change by ourself.
We want business card modern and minimalist but that looks professional.
We will print it in 300 gr soft-touch.
Why not a white side with the logo and a red/grey side with the content?
Why not a grey side and a red side like our logo?
I am sure that you have better idea than ours that's the reason we come here.

Who we are:
We are a private label company in cosmetics based in Switzerland. We work in BtoB. We make skin care products for other brands.

Target Market(s)

B to B - Worldwide - any gender

Industry/Entity Type

Cosmetics

Contact Information for Business Card

Side 1:
Logo
Your Swiss Private Label Manufacturer or www.velmorabelle.ch

Side 2:
Name and surname (Example: Lucien Marchetaz)
Job Description (General Manager)
Telephone (+41 32 918 64 00)
Direct (+41 32 918 64 64)
Email (lucien.marchetaz@velmorabelle.ch)
Chemin des Prés-Fleuris 14, 2000 Neuchâtel, Switzerland
www.velmorabelle.ch

Font styles to use
Serif
Sans Serif

Requirements
Must have
• You can use 4 colors: white, red, grey and/or black .
Should not have
• Too much colors, too much things. We want it simple!

```html
<!DOCTYPE html>
<html lang="en">
<head>
<meta charset="utf-8">
<title>Velmorabelle – Business Card</title>
<link href="https://fonts.googleapis.com/css2?family=Montserrat:wght@300;400;500;800&display=swap" rel="stylesheet">
<style>
  :root {
    --page: #ececec;
    --card-white: #f4f4f4;
    --brand-red: #cf283b;
    --brand-grey: #a9a7a8;
    --text-grey: #6f6f70;
    --text-dark: #555556;
    --rule: #c9c9c9;
  }
  * { margin: 0; padding: 0; box-sizing: border-box; }
  html, body { width: 1200px; height: 1161px; overflow: hidden; }
  body {
    background: var(--page);
    font-family: "Montserrat", sans-serif;
    display: flex;
    align-items: center;
    justify-content: center;
    gap: 48px;
  }
  .card {
    width: 540px;
    height: 310px;
    position: relative;
    box-shadow: 0 2px 6px rgba(0,0,0,.12);
    overflow: hidden;
  }

  /* Front side */
  .card--front {
    background: var(--card-white);
    display: flex;
    align-items: center;
    padding: 0 30px;
  }
  .brand-mark {
    width: 240px;
    display: flex;
    align-items: center;
    gap: 10px;
  }
  .brand-mark__square {
    width: 14px; height: 14px;
    background: var(--brand-red);
    flex: none;
  }
  .brand-mark__name {
    font-weight: 300;
    font-size: 30px;
    letter-spacing: 2px;
    color: var(--brand-red);
  }
  .divider {
    width: 1px;
    height: 150px;
    background: var(--rule);
    margin: 0 24px 0 14px;
  }
  .contact { color: var(--text-grey); }
  .contact__name {
    font-weight: 800;
    font-size: 19px;
    color: var(--text-dark);
  }
  .contact__role {
    font-size: 12px;
    margin-bottom: 10px;
  }
  .contact__address {
    font-size: 11.5px;
    line-height: 1.45;
    margin-bottom: 8px;
  }
  .contact__list { list-style: none; font-size: 11.5px; line-height: 1.55; }
  .contact__list li { display: flex; align-items: center; gap: 8px; }
  .contact__list .icon { width: 11px; height: 11px; flex: none; }
  .contact__list .icon--blank { visibility: hidden; }

  /* Back side */
  .card--back {
    display: flex;
    align-items: center;
    justify-content: center;
  }
  .quilt-pattern {
    position: absolute;
    inset: 0;
    background: var(--brand-red);
  }
  .back-logo {
    position: relative;
    display: flex;
    align-items: center;
    gap: 12px;
    padding: 18px 30px;
    background: var(--card-white);
  }
  .back-logo .brand-mark__name { font-size: 32px; }
</style>
</head>
<body>

  <section class="card card--front" aria-label="Business card, front">
    <div class="brand-mark">
      <span class="brand-mark__square"></span>
      <span class="brand-mark__name">Velmorabelle</span>
    </div>
    <div class="divider"></div>
    <div class="contact">
      <p class="contact__name">Adrien KESSLER</p>
      <p class="contact__role">Managing Partner</p>
      <p class="contact__address">412 Alderbrook Line 7 East<br>Corwen ON, Canada, K2B 4L8</p>
      <ul class="contact__list">
        <li>
          <svg class="icon" viewBox="0 0 12 12"><path d="M3 1 L5 3.5 L4 4.8 Q5 7 7.2 8 L8.5 7 L11 9 L9.5 11 Q4 10.5 1 3 Z" fill="var(--brand-red)"/></svg>
          000 000 0000
        </li>
        <li>
          <svg class="icon" viewBox="0 0 12 12"><rect x="2" y="1" width="8" height="4" fill="var(--brand-red)"/><rect x="0.5" y="5" width="11" height="5" rx="1" fill="var(--brand-red)"/></svg>
          000 000 0000
        </li>
        <li>
          <svg class="icon" viewBox="0 0 12 12"><rect x="0.7" y="2.2" width="10.6" height="7.6" fill="none" stroke="var(--brand-red)" stroke-width="1.2"/><path d="M0.7 2.2 L6 6.5 L11.3 2.2" fill="none" stroke="var(--brand-red)" stroke-width="1.2"/></svg>
          info@velmorabelle.com
        </li>
        <li>
          <svg class="icon" viewBox="0 0 12 12"><circle cx="6" cy="6" r="5" fill="none" stroke="var(--brand-red)" stroke-width="1.1"/><ellipse cx="6" cy="6" rx="2.2" ry="5" fill="none" stroke="var(--brand-red)" stroke-width="1"/><path d="M1 6 H11" stroke="var(--brand-red)" stroke-width="1"/></svg>
          www.velmorabelle.com
        </li>
      </ul>
    </div>
  </section>

  <section class="card card--back" aria-label="Business card, back">
    <div class="quilt-pattern" role="img" aria-label="Red quilted diamond pattern with white dotted lines"></div>
    <div class="back-logo">
      <span class="brand-mark__square"></span>
      <span class="brand-mark__name">Velmorabelle</span>
    </div>
  </section>

</body>
</html>
```